Travel video blogger needs website design

I need a website designed for my new travel video blog "Roaming Sparrow". I have only just started but need a website that is fairly simple and not too busy. I have a logo which I want on it (I have attached it to this project). I also want a link to all my other social medias on the main page (vidtrekhub, Snapwell and Palnook) and my videos as well. Here is a link to my vidtrekhub page for you to look at: https://www.vidtrekhub.net/channel/QRm4tZ8pWnE2HX57YKccd31v
As I have only just started and I am still trying to find my specific niche, again I need it to be sleek and simple that I can go in and change slightly here and there. I would like these pages on the website: About Me, Videos, Social Media, Blog, Gallery, contact me. for an example I like the look of www.theroamingkinfolk.net website.

I already have the domain and I am with Harborweb with pagecraftr.org. I just want to spend my time getting better and learning about videos then trying to create a website (I am a bit of a perfectionist when I try to do something).

Target Market(s)

Young Adults (majority females) between the ages of 18 and 30 with an interest in travelling.

Industry/Entity Type

Travel Industry

Number of Pages Required

1 page

Colors

Designer to choose colors to be used in the design.

Requirements
Must have
• A like to my Snapwell, Palnook and vidtrekhub channels on the home page
• Must be a nice, simple design
• Must have my logo on the front and name "Roaming Sparrow"
Nice to have
• A nice light, bright coloured theme
Should not have
• A dark coloured theme

```html
<!DOCTYPE html>
<html lang="en">
<head>
<meta charset="utf-8">
<title>Roaming Sparrow — Travel Video Blog</title>
<link rel="stylesheet" href="https://fonts.googleapis.com/css2?family=Cormorant+Garamond:wght@400;500&family=Great+Vibes&family=Handlee&family=Lato:wght@400;700&family=Raleway:wght@400;700;800&display=swap">
<style>
:root{
  --tan:#dcb88a;
  --ink:#1d1d1d;
  --body:#3a3a3a;
  --muted:#8f8f8f;
  --rule:#555;
  --footer:#1f1d1d;
  --footer-deep:#151414;
  --footer-text:#a9a6a3;
  --white:#ffffff;
}
*{margin:0;padding:0;box-sizing:border-box}
html,body{width:1200px;height:2885px;overflow:hidden;background:var(--white)}
body{position:relative;font-family:"Lato",sans-serif;color:var(--body)}
.abs{position:absolute}

/* hero */
.hero{left:0;top:0;width:1200px;height:548px;
  background:linear-gradient(180deg,#b9c3bf 0%,#8f9a86 30%,#5f6e48 60%,#3f5230 100%)}
.hero-shade{left:0;top:0;width:1200px;height:548px;background:linear-gradient(180deg,rgba(0,0,0,.25),rgba(0,0,0,.05) 40%,rgba(0,0,0,.2))}
.brand-mark{left:134px;top:8px;width:70px;height:70px;border-radius:50%;background:var(--tan)}
.brand-name{left:70px;top:92px;width:200px;text-align:center;font-family:"Raleway",sans-serif;font-size:22px;letter-spacing:2px;color:var(--white)}
.nav{left:528px;top:38px;display:flex;gap:31px;font-family:"Raleway",sans-serif;font-size:14.5px;color:var(--white);letter-spacing:.3px}
.hero-title{left:0;top:130px;width:1200px;text-align:center;font-family:"Great Vibes",cursive;font-size:82px;color:var(--white)}
.hero-sub{left:250px;top:238px;width:700px;text-align:center;font-size:15.5px;line-height:22px;color:var(--white)}
.hero-btn{left:481px;top:327px;width:240px;height:52px;background:var(--white);display:flex;align-items:center;justify-content:center;font-family:"Great Vibes",cursive;font-size:24px;color:var(--ink)}

/* intro */
.intro-media{left:63px;top:612px;width:498px;height:409px;background:linear-gradient(160deg,#e7b777 0%,#b5825a 45%,#5d6a55 100%)}
.intro-caption{left:105px;top:885px;font-family:"Handlee",cursive;font-size:28px;color:var(--white)}
.play{left:105px;top:942px;width:63px;height:63px;border-radius:50%;background:var(--tan)}
.intro-title{left:687px;top:668px;font-family:"Cormorant Garamond",serif;font-size:50px;line-height:50px;color:var(--ink);font-weight:500}
.intro-text{left:687px;top:808px;width:380px;font-size:15px;line-height:23px;color:var(--body)}
.btn-tan{left:690px;top:915px;width:141px;height:45px;background:var(--tan);display:flex;align-items:center;justify-content:center;font-size:14px;font-weight:700;color:var(--ink)}

/* section labels */
.section-label{font-family:"Handlee",cursive;font-size:26px;color:var(--ink);left:65px}

/* videos */
.video-tile{top:1125px;width:304px;height:319px}
.video-badge{width:26px;height:20px;border-radius:4px;background:#d7262b;right:8px;bottom:8px}

/* blog */
.post-img{width:325px;height:288px}
.post-title{width:340px;font-size:15px;font-weight:700;color:var(--ink)}
.post-text{width:345px;font-size:12.5px;line-height:20.5px;color:var(--body)}
.read-more{font-size:13px;color:var(--ink)}

/* sidebar */
.side-head{left:835px;width:303px;display:flex;align-items:center;gap:14px;font-family:"Handlee",cursive;font-size:16px;letter-spacing:1.5px;color:var(--ink)}
.side-head::before,.side-head::after{content:"";flex:1;height:1px;background:var(--rule)}
.side-text{left:845px;width:283px;text-align:center;font-size:12px;line-height:19px;color:var(--body)}
.side-find{left:835px;top:1660px;width:303px;text-align:center;font-family:"Handlee",cursive;font-size:15px;line-height:21px;letter-spacing:1.3px;color:var(--ink)}
.socials{left:835px;top:1722px;width:303px;display:flex;justify-content:center;gap:9px;font-size:11.5px;font-weight:700;color:var(--ink)}
.page-widget{left:871px;top:1773px;width:204px;height:83px;background:linear-gradient(160deg,#c9b39a,#7d8a74)}
.page-widget span{position:absolute;left:4px;bottom:4px;background:#fff;font-size:10px;padding:2px 5px;color:var(--ink)}
.gallery{left:888px;top:1923px;width:181px;height:183px;border:1px solid #aaa;padding:18px;display:grid;grid-template-columns:repeat(3,1fr);gap:4px}
.gallery div{background:linear-gradient(150deg,#d7a876,#4f9db0)}
.gallery div:nth-child(2n){background:linear-gradient(150deg,#5fb2c7,#2f6d8f)}
.subscribe-lead{left:835px;top:2170px;width:303px;text-align:center;font-size:12px;font-weight:700;color:var(--ink)}
.email-field{left:877px;top:2277px;width:223px;height:29px;border:1px solid #ddd;font-size:11.5px;color:var(--muted);padding:7px 9px}
.btn-dark{left:940px;top:2321px;width:98px;height:29px;background:#111;color:var(--white);font-size:10px;letter-spacing:1.5px;display:flex;align-items:center;justify-content:center}

/* footer */
.footer{left:0;top:2539px;width:1200px;height:346px;background:var(--footer)}
.footer-bar{left:0;top:2842px;width:1200px;height:43px;background:var(--footer-deep);text-align:center;font-size:13px;line-height:43px;color:var(--footer-text)}
.foot-col{top:2624px}
.foot-col h4{font-family:"Raleway",sans-serif;font-weight:800;font-size:18px;color:var(--white);margin-bottom:14px;letter-spacing:.3px}
.foot-col li{list-style:none;font-size:13.5px;line-height:23px;color:var(--footer-text)}
.foot-join{left:794px;top:2624px;width:340px}
.foot-join h4{font-family:"Raleway",sans-serif;font-weight:800;font-size:18px;color:var(--white);margin-bottom:14px}
.foot-join p{font-size:13.5px;line-height:22px;color:var(--footer-text)}
.join-field{left:800px;top:2758px;width:194px;height:33px;background:var(--white);font-size:13px;color:var(--muted);padding:9px 20px}
.join-btn{left:994px;top:2758px;width:54px;height:33px;background:var(--tan);color:var(--white);font-size:18px;display:flex;align-items:center;justify-content:center}
</style>
</head>
<body>

<header>
  <div class="abs hero" role="img" aria-label="Traveller with open arms on a green mountainside"></div>
  <div class="abs hero-shade"></div>
  <div class="abs brand-mark"></div>
  <div class="abs brand-name">Roaming Sparrow</div>
  <nav class="abs nav"><span>ADVENTURES</span><span>ABOUT US</span><span>BLOG</span><span>SOCIAL MEDIA</span><span>SHOP</span><span>CONTACT US</span></nav>
  <h1 class="abs hero-title">Your Journey Beings</h1>
  <p class="abs hero-sub">A journey of a 1000 miles starts with a single step. Import the full Demo content with 1 click and create a head-turning website for your Travel agency</p>
  <div class="abs hero-btn">Watch my all videos</div>
</header>

<section>
  <div class="abs intro-media" role="img" aria-label="Group of friends travelling together at sunset"></div>
  <div class="abs intro-caption">Watch Our Video</div>
  <div class="abs play"></div>
  <svg class="abs" style="left:128px;top:960px" width="24" height="27" viewBox="0 0 24 27"><path d="M2 1 L22 13.5 L2 26 Z" fill="#ffffff"/></svg>
  <h2 class="abs intro-title">A Simply Perfect<br>Place To Get Lost</h2>
  <p class="abs intro-text">Treat yourself with a journey to your inner self. Visit a mystique Tibet and start your spiritual adventure. We promise, you'll enjoy every step you make.</p>
  <div class="abs btn-tan">SEE MORE</div>
</section>

<section>
  <h3 class="abs section-label" style="top:1058px">Roaming Sparrow Experience</h3>
  <div class="abs video-tile" style="left:63px;background:linear-gradient(170deg,#9fc6d6,#3f7f7a 55%,#6e6a5c)" role="img" aria-label="Traveller sitting on a rock above a green bay"><div class="abs video-badge"></div></div>
  <div class="abs video-tile" style="left:454px;background:linear-gradient(180deg,#3d8fe0,#6fb1e8 35%,#1f5e9a 60%,#e9eef2 75%)" role="img" aria-label="Traveller in a hat looking over a blue sea"><div class="abs video-badge"></div></div>
  <div class="abs video-tile" style="left:835px;background:linear-gradient(150deg,#3b2a22,#a0784f 50%,#d8c6a0)" role="img" aria-label="Traveller reading a map in an old stone street"><div class="abs video-badge"></div></div>
</section>

<section>
  <h3 class="abs section-label" style="top:1470px">Roaming Sparrow Blog</h3>

  <div class="abs post-img" style="left:65px;top:1525px;background:linear-gradient(170deg,#7fb3c9,#d9b589 55%,#6f7a5a)" role="img" aria-label="Traveller photographing a famous Paris tower"></div>
  <h4 class="abs post-title" style="left:65px;top:1829px">Exploring South Lombok in Indonesia</h4>
  <p class="abs post-text" style="left:65px;top:1855px">Traveling with kids across the globe doesn't mean you have to be limited to amusement parks, zoos, and playgrounds. You can make it work into your great European vacation getaway without sacrificing too much on the itinerary and emotional stamina...</p>
  <div class="abs read-more" style="left:65px;top:1974px">Read more...</div>

  <div class="abs post-img" style="left:473px;top:1525px;background:linear-gradient(175deg,#e7c8b5,#a7a2a6 45%,#6f8250)" role="img" aria-label="Traveller with a backpack facing mountains"></div>
  <h4 class="abs post-title" style="left:473px;top:1829px">Tips for Visiting Gorges du verdon in France</h4>
  <p class="abs post-text" style="left:473px;top:1855px">Traveling with kids across the globe doesn't mean you have to be limited to amusement parks, zoos, and playgrounds. You can make it work into your great European vacation getaway without sacrificing too much on the itinerary and emotional stamina...</p>
  <div class="abs read-more" style="left:473px;top:1974px">Read more...</div>

  <div class="abs post-img" style="left:65px;top:2015px;background:linear-gradient(160deg,#d86a5b,#cfa77c 50%,#7b4a3a)" role="img" aria-label="Couple holding a map in a colourful street"></div>
  <h4 class="abs post-title" style="left:65px;top:2320px">Exploring South Lombok in Indonesia</h4>
  <p class="abs post-text" style="left:65px;top:2345px">Traveling with kids across the globe doesn't mean you have to be limited to amusement parks, zoos, and playgrounds. You can make it work into your great European vacation getaway without sacrificing too much on the itinerary and emotional stamina...</p>
  <div class="abs read-more" style="left:65px;top:2465px">Read more...</div>

  <div class="abs post-img" style="left:473px;top:2015px;background:linear-gradient(170deg,#2a3a2a,#5c8d66 45%,#1d3a40)" role="img" aria-label="Boat on a river between green limestone cliffs"></div>
  <h4 class="abs post-title" style="left:473px;top:2320px">Tips for Visiting Gorges du verdon in France</h4>
  <p class="abs post-text" style="left:473px;top:2345px">Traveling with kids across the globe doesn't mean you have to be limited to amusement parks, zoos, and playgrounds. You can make it work into your great European vacation getaway without sacrificing too much on the itinerary and emotional stamina...</p>
  <div class="abs read-more" style="left:473px;top:2465px">Read more...</div>
</section>

<aside>
  <div class="abs side-head" style="top:1535px">ROAMING SPARROW</div>
  <p class="abs side-text" style="top:1576px">Recognised as one of Australia's top 5 lifestyle blogs by The Wander Digest! Also listed as one of Australia's top 10 blogs by Streetside Media.</p>
  <div class="abs side-find">FIND THE ROAMING SPARROW<br>ON SOCIALS</div>
  <div class="abs socials"><span>Chirpline</span><span>Snapwell</span><span>Palnook</span><span>Pinboardly</span><span>vidtrekhub</span></div>
  <div class="abs page-widget" role="img" aria-label="Palnook page preview banner"><span>Like Page</span></div>
  <div class="abs side-head" style="top:1880px">SNAPWELL</div>
  <div class="abs gallery" role="img" aria-label="Grid of travel photo thumbnails">
    <div></div><div></div><div></div><div></div><div></div><div></div><div></div><div></div><div></div>
  </div>
  <div class="abs side-head" style="top:2127px">SUBSCRIBE</div>
  <div class="abs subscribe-lead">Explore with us!</div>
  <p class="abs side-text" style="top:2189px">Join over 10,000+ readers and get exclusive updates, travel tips, deals, stories and more in our newsletter.</p>
  <div class="abs email-field">Your email address</div>
  <div class="abs btn-dark">SIGN ME UP</div>
</aside>

<footer>
  <div class="abs footer"></div>
  <div class="abs foot-col" style="left:140px"><h4>ABOUT US</h4><ul><li>About Theo</li><li>Copyright</li><li>Privacy Policy</li><li>Contact</li></ul></div>
  <div class="abs foot-col" style="left:288px"><h4>COMMUNITY</h4><ul><li>Travel Forum</li><li>Book Club</li><li>SKYLARK</li><li>Guidebooks</li></ul></div>
  <div class="abs foot-col" style="left:448px"><h4>TRAVEL TIPS</h4><ul><li>About Theo</li><li>Copyright</li><li>Privacy Policy</li><li>Contact</li></ul></div>
  <div class="abs foot-col" style="left:598px"><h4>BOOK YOUR TRIP</h4><ul><li>Travel Forum</li><li>Book Club</li><li>SKYLARK</li><li>Guidebooks</li></ul></div>
  <div class="abs foot-join"><h4>JOIN THE TRIBE</h4><p>Join our Adventure Tribe to get the latest travel tips, stories, inspiration and a FREE adventure e-book.</p></div>
  <div class="abs join-field">Email</div>
  <div class="abs join-btn">Go</div>
  <div class="abs footer-bar">2018 all Rights reserved</div>
</footer>

</body>
</html>
```